Create new graphics and layout for VELMORA Showcases One Pager

VELMORA Technology. is a revolutionary platform that uses high frequency tones (known as VELMORA packets) imperceptible to the human ear. Using Quietwave Signals® technology, VELMORA LLC embeds information on an audio file for a more targeted, enhanced user experience via music, video, text, virtual reality, augmented reality, and other content. We want to make 1 pager creatively communicate these ideas and opportunities. Additionally we want the graphics to elicit trust and brand recognition. The draft one pager we provided does not achieve this goal so we encourage you to provide your best ideas, using the brand guidelines provided.

Brand and Typesetting is provided in the Branding Guidelines document
Current draft 1 pager is attached
VIsuals should be engaging but not too distracting.
We are open to all other images and overall design, while maintaining the colors and typography stated in the brand guidelines. Please be creative but again professional and demonstrate that VELMORA is a high tech, innovative and creative firm.
We are re-doing the copy so you can use placeholder text.

You can create your design in Powerpoint, Photoshop or Illustrator.

```html
<!DOCTYPE html>
<html lang="en">
<head>
<meta charset="utf-8">
<title>VELMORA Technology One Pager</title>
<link rel="stylesheet" href="https://fonts.googleapis.com/css2?family=Montserrat:wght@400;500;600;700;800&display=swap">
<style>
  :root{
    --navy:#0a1449;
    --navy-deep:#06103c;
    --blue:#2f86ee;
    --sky:#4fb8ff;
    --indigo:#3d3bb8;
    --purple:#3a33b3;
    --ink:#1a1f4a;
    --white:#ffffff;
    --paper:#f3f4f8;
    --card-line:rgba(255,255,255,0.45);
  }
  *{margin:0;padding:0;box-sizing:border-box}
  html,body{width:884px;height:1200px;overflow:hidden;background:var(--paper)}
  body{font-family:"Montserrat",sans-serif;position:relative}
  .page{position:absolute;inset:0;width:884px;height:1200px;overflow:hidden;background:var(--paper)}
  .abs{position:absolute}

  .top-band{left:0;top:0;width:884px;height:112px;background:var(--navy)}
  .hero-panel{left:0;top:111px;width:884px;height:313px;
    background:linear-gradient(100deg,var(--blue) 0%,#3a63d8 55%,var(--indigo) 100%)}
  .hero-art{left:0;top:0;width:540px;height:560px}

  .brand{right:46px;top:28px;color:var(--white);font-weight:500;font-size:44px;letter-spacing:8px;line-height:1}

  .hero-title{right:46px;top:160px;text-align:right;color:var(--white);font-weight:700;line-height:1}
  .hero-title .t1{display:block;font-size:42px}
  .hero-title .t2{display:block;font-size:44px;font-weight:600;margin-top:10px}
  .hero-rule{left:474px;top:304px;width:363px;height:2px;background:var(--white)}
  .hero-copy{right:46px;top:328px;width:410px;text-align:right;color:var(--white);font-size:14.2px;line-height:21.5px;font-weight:400}

  .platform-head{right:46px;top:482px;color:var(--purple);font-weight:800;font-size:25px;letter-spacing:-0.3px}
  .platform-copy{left:47px;top:516px;width:790px;color:var(--ink);font-size:15.1px;line-height:21.6px;text-align:justify}

  .dark-wave{left:0;top:610px;width:884px;height:510px}

  .section-title{left:0;top:720px;width:884px;text-align:center;color:var(--white);font-weight:800;font-size:33px;letter-spacing:-0.3px}

  .card{width:169px;height:118px;border:1px solid var(--card-line);border-radius:9px;
    display:flex;align-items:flex-end;justify-content:center;padding-bottom:26px;
    color:var(--white);font-size:16.5px;line-height:20px;text-align:center}
  .icon-tile{width:58px;height:50px;border-radius:8px;
    background:linear-gradient(135deg,#3d7de8,#3446c9);display:flex;align-items:center;justify-content:center}
  .icon-tile svg{width:32px;height:32px;fill:none;stroke:var(--white);stroke-width:1.6;stroke-linecap:round;stroke-linejoin:round}

  .footer{left:0;top:1115px;width:884px;height:85px;background:var(--white)}
  .contact{top:1143px;color:var(--navy);font-weight:700;font-size:16px}
  .divider{top:1130px;width:1px;height:52px;background:var(--navy)}
  .social-pill{left:650px;top:1129px;width:234px;height:54px;border-radius:27px 0 0 27px;
    background:linear-gradient(90deg,#3446c9,#4a5bd8);display:flex;align-items:center;padding-left:12px;gap:9px}
  .social-dot{width:25px;height:25px;border-radius:50%;border:2px solid var(--white)}
</style>
</head>
<body>
<main class="page">

  <div class="abs top-band"></div>
  <div class="abs hero-panel"></div>

  <svg class="abs hero-art" viewBox="0 0 540 560" role="img" aria-label="Illustration: a person with a megaphone jumping beside a large phone showing a target and clouds">
    <defs>
      <linearGradient id="heroBlob" x1="0" y1="0" x2="1" y2="1">
        <stop offset="0" stop-color="#3d9bff"/>
        <stop offset="0.6" stop-color="#2f6fe0"/>
        <stop offset="1" stop-color="#4536c0"/>
      </linearGradient>
    </defs>
    <path d="M0 0 L60 0 C120 60 200 80 290 70 C420 60 480 140 470 260 C460 390 380 470 260 492 C160 510 70 490 0 460 Z" fill="url(#heroBlob)"/>
  </svg>

  <div class="abs brand">VELMORA</div>

  <h1 class="abs hero-title"><span class="t1">VELMORA®</span><span class="t2">TECHNOLOGY</span></h1>
  <div class="abs hero-rule"></div>
  <p class="abs hero-copy">VELMORA® technology is a revolutionary platform that uses high-frequency tones imperceptible to the human ear.</p>

  <h2 class="abs platform-head">OUR REVOLUTIONARY PLATFORM</h2>
  <p class="abs platform-copy">Whether you’re marketing a product, selling a service, or looking to close a deal – pinpoint your target market and quickly modify your campaigns to reach consumers silently and securely. Our platform goes far beyond basic ad optimization to deliver individualized content using embedded tones that immediately increases engagement over any communication medium.</p>

  <svg class="abs dark-wave" viewBox="0 0 884 510" preserveAspectRatio="none" aria-hidden="true">
    <defs>
      <linearGradient id="edgeBlue" x1="0" y1="0" x2="1" y2="0">
        <stop offset="0" stop-color="#3d9bff"/>
        <stop offset="1" stop-color="#3a40c4"/>
      </linearGradient>
    </defs>
    <path d="M0 20 C60 18 130 36 185 64 L0 64 Z" fill="#3d9bff"/>
    <path d="M560 60 C680 30 800 16 884 14 L884 60 Z" fill="url(#edgeBlue)"/>
    <path d="M0 40 C100 40 180 86 290 86 C420 86 520 46 680 33 C780 27 850 28 884 30 L884 510 L0 510 Z" fill="var(--navy)"/>
  </svg>

  <h2 class="abs section-title">VELMORA® REVOLUTIONARY PLATFORM</h2>

  <!-- Row 1 -->
  <div class="abs card" style="left:46px;top:813px">Corporate<br>Subscriptions</div>
  <div class="abs card" style="left:258px;top:813px">AD Tech<br>Licensing</div>
  <div class="abs card" style="left:465px;top:813px">Platform<br>Integrations</div>
  <div class="abs card" style="left:669px;top:813px">Technology<br>Licensing</div>

  <div class="abs icon-tile" style="left:101px;top:792px"><svg viewBox="0 0 32 32"><rect x="5" y="5" width="22" height="14" rx="1"/><path d="M9 10h8M9 14h5M14 30v-9a2 2 0 0 1 4 0v5"/></svg></div>
  <div class="abs icon-tile" style="left:313px;top:792px"><svg viewBox="0 0 32 32"><rect x="5" y="5" width="22" height="20" rx="1"/><path d="M9 11h7M9 15h5"/><circle cx="20" cy="16" r="4"/><path d="M18 20l-1 7 3-2 3 2-1-7"/></svg></div>
  <div class="abs icon-tile" style="left:520px;top:792px"><svg viewBox="0 0 32 32"><circle cx="16" cy="16" r="4"/><circle cx="6" cy="6" r="2.5"/><circle cx="26" cy="6" r="2.5"/><circle cx="6" cy="26" r="2.5"/><circle cx="26" cy="26" r="2.5"/><path d="M8 8l5 5M24 8l-5 5M8 24l5-5M24 24l-5-5"/></svg></div>
  <div class="abs icon-tile" style="left:724px;top:792px"><svg viewBox="0 0 32 32"><rect x="9" y="4" width="16" height="24" rx="2"/><circle cx="8" cy="12" r="4"/><path d="M13 20l3-3 3 3 3-4"/></svg></div>

  <!-- Row 2 -->
  <div class="abs card" style="left:46px;top:970px">Advertising<br>Campaigns</div>
  <div class="abs card" style="left:258px;top:970px">NFT<br>Security</div>
  <div class="abs card" style="left:465px;top:970px">Digital Rights<br>Management</div>
  <div class="abs card" style="left:669px;top:970px">Reporting<br>and Analytics</div>

  <div class="abs icon-tile" style="left:101px;top:948px"><svg viewBox="0 0 32 32"><path d="M8 22l10-8v14z"/><path d="M4 6h6M4 10h6M20 6h8v8h-8z"/><circle cx="24" cy="22" r="3"/></svg></div>
  <div class="abs icon-tile" style="left:313px;top:948px"><svg viewBox="0 0 32 32"><path d="M16 3l11 4v8c0 7-5 12-11 14C10 27 5 22 5 15V7z"/><path d="M11 16l4 4 7-8"/></svg></div>
  <div class="abs icon-tile" style="left:520px;top:948px"><svg viewBox="0 0 32 32"><rect x="10" y="3" width="14" height="26" rx="2"/><circle cx="17" cy="15" r="4"/><path d="M4 10h4M4 16h4M4 22h4"/></svg></div>
  <div class="abs icon-tile" style="left:724px;top:948px"><svg viewBox="0 0 32 32"><rect x="3" y="7" width="26" height="18" rx="1"/><path d="M7 12h6M7 16h8M7 20h5"/><circle cx="22" cy="16" r="4"/></svg></div>

  <!-- Footer -->
  <div class="abs footer"></div>
  <div class="abs contact" style="left:52px">1-866-555-0147</div>
  <div class="abs divider" style="left:223px"></div>
  <div class="abs contact" style="left:242px">info@velmoratech.com</div>
  <div class="abs divider" style="left:440px"></div>
  <div class="abs contact" style="left:455px">www.velmoratech.com</div>
  <div class="abs social-pill">
    <span class="social-dot"></span><span class="social-dot"></span><span class="social-dot"></span><span class="social-dot"></span><span class="social-dot"></span>
  </div>

</main>
</body>
</html>
```